School Signage

I am wanting designs for signs completed that prompt students of the school requirements for hats, preparation and play.

I've uploaded rough examples of what we're after, but we would like them stylised and better than the example, including:
- A stylised logo/graphic for the 'Mervale 1, 2, 3'
- Clear, crisp signage for the words.
- Graphics that reinforce the message of the sign.

We're after three signs:
- One that will be located on the oval to prompt hat use.
- One that will be near the entry prompting the morning routine (please make this one landscape with instructions for 'on time' on one side, and 'late' on the other).
- One that will be located within the school prompting readiness for class.

```html
<!DOCTYPE html>
<html lang="en">
<head>
<meta charset="utf-8">
<title>Mervale 1, 2, 3 – School Signage</title>
<link rel="stylesheet" href="https://fonts.googleapis.com/css2?family=Montserrat:wght@700;800;900&family=Arimo:wght@400;700&family=Luckiest+Guy&display=swap">
<style>
  :root{
    --green:#1c3d21;
    --yellow:#e9e400;
    --white:#ffffff;
    --stage:#c9cacb;
    --pattern:#d6e9f2;
    --pattern-dark:#8fa595;
  }
  *{margin:0;padding:0;box-sizing:border-box}
  html,body{width:1200px;height:1139px;overflow:hidden}
  body{background:var(--stage);position:relative;font-family:"Montserrat",sans-serif;color:var(--green)}
  .frame{position:absolute;inset:0;border:2px solid #555}
  .sign{position:absolute;background:var(--white);overflow:hidden;box-shadow:0 2px 6px rgba(0,0,0,.25)}
  .sign svg.shape{position:absolute;left:0;top:0}
  .abs{position:absolute}
  .pattern{position:absolute;border-radius:50%;background:radial-gradient(circle,var(--pattern) 0%,rgba(214,233,242,.5) 55%,rgba(214,233,242,0) 72%)}
  .pattern.low{border-radius:40% 60% 0 0;background:linear-gradient(90deg,rgba(143,165,149,.55),rgba(143,165,149,0))}

  /* portrait signs */
  .portrait{width:358px;height:505px;top:45px}
  .hats{left:161px}
  .ready{left:659px}
  .title{font-weight:900;line-height:1.05;text-transform:uppercase}
  .hats .title{left:19px;top:36px;font-size:20px}
  .ready .title{left:19px;top:36px;font-size:32px}
  .tagline{height:20px;background:var(--green);color:var(--white);font-family:"Arimo",sans-serif;font-weight:700;font-size:11px;letter-spacing:3.6px;line-height:20px;padding-left:19px;border-radius:0 10px 10px 0}
  .icon{position:absolute}
  .pill{position:absolute;background:var(--green);color:var(--white);font-weight:800;display:flex;align-items:center}
  .hats .pill{left:132px;width:180px;height:30px;font-size:20px;padding-left:28px;border-radius:4px 15px 15px 4px}
  .ready .pill{left:106px;font-size:17px;line-height:1.05;padding-left:10px;border-radius:0 24px 24px 0}
  .footer-text{color:var(--white);font-family:"Arimo",sans-serif;font-weight:700;white-space:nowrap;text-align:right}
  .footer-text small{display:block;color:var(--yellow);font-weight:400}
  .portrait .footer-text{right:91px;top:446px;font-size:18px;line-height:1}
  .portrait .footer-text small{font-size:13.5px;margin-top:2px}
  .brand{position:absolute;display:flex;flex-direction:column;align-items:center;gap:3px;color:var(--yellow);font-weight:800;font-size:11px;text-transform:uppercase}
  .brand .dot{width:30px;height:30px;border-radius:50%;background:var(--yellow)}

  /* landscape sign */
  .routine{left:237px;top:581px;width:726px;height:512px}
  .routine .header{position:absolute;left:0;top:0;width:726px;height:103px;background:var(--green);color:var(--white);text-align:center}
  .routine h1{font-weight:900;font-size:56px;letter-spacing:-.5px;line-height:1;padding-top:14px}
  .routine .header p{font-family:"Arimo",sans-serif;font-weight:700;font-size:15px;letter-spacing:5px;margin-top:7px}
  .status{position:absolute;top:137px;height:31px;background:var(--green);color:var(--white);font-weight:800;font-size:17px;line-height:31px}
  .status.on{left:0;width:166px;padding-left:45px;border-radius:0 16px 16px 0}
  .status.late{right:0;width:211px;padding-left:22px;border-radius:16px 0 0 16px}
  .motto{position:absolute;left:188px;top:122px;width:350px;text-align:center;font-family:"Luckiest Guy","Montserrat",sans-serif;font-weight:400;font-size:29px;line-height:28px;letter-spacing:.5px}
  .step-icon{position:absolute;width:64px;height:64px;border-radius:50%;background:var(--green);border:3px solid var(--white);box-shadow:0 0 0 2px var(--green)}
  .step{position:absolute;font-family:"Arimo",sans-serif;font-weight:700;font-size:12.5px;line-height:16px;text-transform:uppercase;letter-spacing:-.1px}
  .routine .footer-text{right:132px;top:470px;font-size:20px;line-height:1}
  .routine .footer-text small{font-size:15px;margin-top:2px}
  .line{fill:none;stroke:#fff;stroke-width:5;stroke-linecap:round;stroke-linejoin:round}
  .thin{fill:none;stroke:#fff;stroke-width:2.5;stroke-linecap:round;stroke-linejoin:round}
</style>
</head>
<body>
<div class="frame"></div>

<!-- Hats sign -->
<section class="sign portrait hats">
  <div class="pattern" style="left:220px;top:0;width:170px;height:170px" role="img" aria-label="Dot-painting circle ornament"></div>
  <svg class="shape" width="358" height="505" viewBox="0 0 358 505">
    <path d="M0 0H358V6C250 34 140 4 0 30Z" fill="var(--green)"/>
    <path d="M0 430C110 400 230 442 358 412V505H0Z" fill="var(--green)"/>
  </svg>
  <div class="pattern low" style="left:0;top:470px;width:200px;height:35px" role="img" aria-label="Dot-painting band ornament"></div>
  <h2 class="abs title">We wear hats at<br>Mervale when outdoors</h2>
  <div class="abs tagline" style="left:0;top:84px;width:225px">THE MERVALE 1, 2, 3.</div>

  <svg class="icon" style="left:38px;top:125px" width="85" height="85" viewBox="0 0 84 84" role="img" aria-label="Walking icon">
    <circle cx="42" cy="42" r="42" fill="var(--green)"/>
    <circle cx="30" cy="20" r="5" fill="#fff"/>
    <path class="line" d="M30 28L28 46M28 46L22 62M28 46L34 62M29 32L22 42M29 32L36 40"/>
    <circle cx="54" cy="20" r="5" fill="#fff"/>
    <path class="line" d="M54 28L52 46M52 46L46 62M52 46L58 62M53 32L46 40M53 32L60 42"/>
  </svg>
  <div class="pill" style="top:152px">1. WALKING</div>

  <svg class="icon" style="left:38px;top:221px" width="85" height="85" viewBox="0 0 84 84" role="img" aria-label="Sitting icon">
    <circle cx="42" cy="42" r="42" fill="var(--green)"/>
    <circle cx="40" cy="20" r="5" fill="#fff"/>
    <path class="line" d="M40 28L40 46L54 46L54 62M40 33L48 42"/>
    <path class="line" d="M30 28L30 64M30 50L48 50M46 50L46 64"/>
  </svg>
  <div class="pill" style="top:248px">2. SITTING</div>

  <svg class="icon" style="left:38px;top:318px" width="85" height="85" viewBox="0 0 84 84" role="img" aria-label="Playing icon">
    <circle cx="42" cy="42" r="42" fill="var(--green)"/>
    <circle cx="26" cy="22" r="5" fill="#fff"/>
    <path class="line" d="M28 30L34 44M34 44L24 56M34 44L44 52M30 34L20 38M30 34L40 30"/>
    <circle cx="50" cy="60" r="5" fill="#fff"/>
    <circle cx="58" cy="22" r="5" fill="#fff"/>
    <path class="line" d="M58 30L56 46M56 46L62 62M56 46L48 56M57 34L64 40M57 34L50 38"/>
  </svg>
  <div class="pill" style="top:345px">3. PLAYING</div>

  <div class="abs footer-text">Curiosty and Drive<small>Mervale Learner Values</small></div>
  <div class="brand" style="left:275px;top:436px"><span class="dot"></span>Mervale</div>
</section>

<!-- Ready for class sign -->
<section class="sign portrait ready">
  <div class="pattern" style="left:220px;top:0;width:170px;height:170px" role="img" aria-label="Dot-painting circle ornament"></div>
  <svg class="shape" width="358" height="505" viewBox="0 0 358 505">
    <path d="M0 0H358V6C250 34 140 4 0 30Z" fill="var(--green)"/>
    <path d="M0 430C110 400 230 442 358 412V505H0Z" fill="var(--green)"/>
  </svg>
  <div class="pattern low" style="left:0;top:470px;width:200px;height:35px" role="img" aria-label="Dot-painting band ornament"></div>
  <h2 class="abs title">Are you ready<br>for class ?</h2>
  <div class="abs tagline" style="left:0;top:108px;width:224px">THE MERVALE 1, 2, 3.</div>

  <svg class="icon" style="left:17px;top:141px" width="84" height="84" viewBox="0 0 84 84" role="img" aria-label="Laptop icon">
    <circle cx="42" cy="42" r="42" fill="var(--green)"/>
    <rect x="24" y="24" width="36" height="25" rx="2" fill="none" stroke="#fff" stroke-width="3"/>
    <path d="M17 53H67L63 60H21Z" fill="#fff"/>
  </svg>
  <div class="pill" style="top:160px;width:210px;height:46px">1. LAPTOP /<br>&nbsp;&nbsp;&nbsp;&nbsp;WORKBOOK</div>

  <svg class="icon" style="left:17px;top:236px" width="84" height="84" viewBox="0 0 84 84" role="img" aria-label="Phone icon">
    <circle cx="42" cy="42" r="42" fill="var(--green)"/>
    <rect x="30" y="18" width="24" height="44" rx="4" fill="none" stroke="#fff" stroke-width="3"/>
    <circle cx="42" cy="56" r="2" fill="#fff"/>
  </svg>
  <div class="pill" style="top:255px;width:210px;height:47px">2. PHONE IN YOUR</div>

  <svg class="icon" style="left:17px;top:332px" width="84" height="84" viewBox="0 0 84 84" role="img" aria-label="Cap icon">
    <circle cx="42" cy="42" r="42" fill="var(--green)"/>
    <path d="M16 50C16 34 28 26 40 26C54 26 60 36 60 46L70 54C60 58 36 56 16 50Z" fill="#fff"/>
    <path d="M40 26C36 34 34 42 34 52M60 46C50 48 40 50 30 50" fill="none" stroke="var(--green)" stroke-width="2"/>
  </svg>
  <div class="pill" style="top:351px;width:244px;height:47px">3. CORRECT UNIFORM<br>&nbsp;&nbsp;&nbsp;&nbsp;( INCLUDING HAT )</div>

  <div class="abs footer-text">Curiosty and Drive<small>Mervale Learner Values</small></div>
  <div class="brand" style="left:275px;top:436px"><span class="dot"></span>Mervale</div>
</section>

<!-- Morning routine sign -->
<section class="sign routine">
  <div class="pattern" style="left:-20px;top:400px;width:200px;height:150px" role="img" aria-label="Dot-painting circle ornament"></div>
  <svg class="shape" width="726" height="512" viewBox="0 0 726 512">
    <path d="M0 470C200 420 420 500 726 425V512H0Z" fill="var(--green)"/>
  </svg>
  <header class="header">
    <h1>MORNING ROUTINE</h1>
    <p>THE MERVALE 1, 2, 3.</p>
  </header>
  <div class="status on">ON TIME :</div>
  <div class="motto">EARLY IS ON TIME<br>ON TIME IS LATE !</div>
  <div class="status late">RUNNING LATE :</div>

  <svg class="step-icon" style="left:34px;top:195px" viewBox="0 0 64 64" role="img" aria-label="Clock icon">
    <circle cx="32" cy="32" r="22" fill="#fff"/>
    <path d="M32 16V32L42 38" stroke="var(--green)" stroke-width="3" fill="none" stroke-linecap="round"/>
  </svg>
  <p class="step" style="left:114px;top:219px">1. Arrive before 8:30 am</p>
  <svg class="step-icon" style="left:34px;top:274px" viewBox="0 0 64 64" role="img" aria-label="Lockers icon">
    <g fill="none" stroke="#fff" stroke-width="2"><rect x="16" y="16" width="10" height="32"/><rect x="27" y="16" width="10" height="32"/><rect x="38" y="16" width="10" height="32"/></g>
  </svg>
  <p class="step" style="left:114px;top:290px">2. Drop bag at locker and<br>collect learning materials</p>
  <svg class="step-icon" style="left:34px;top:354px" viewBox="0 0 64 64" role="img" aria-label="Backpack icon">
    <path class="thin" d="M26 18Q32 10 38 18"/>
    <rect class="thin" x="20" y="18" width="24" height="30" rx="7"/>
    <rect class="thin" x="25" y="34" width="14" height="10" rx="2"/>
  </svg>
  <p class="step" style="left:114px;top:370px">3. Arrive at home group/<br>house assembly before 8:40 am</p>

  <svg class="step-icon" style="left:412px;top:195px" viewBox="0 0 64 64" role="img" aria-label="School building icon">
    <path d="M13 26L32 14L51 26Z" fill="#fff"/>
    <rect class="thin" x="16" y="26" width="32" height="22"/>
    <g fill="#fff"><rect x="20" y="30" width="5" height="5"/><rect x="29.5" y="30" width="5" height="5"/><rect x="39" y="30" width="5" height="5"/><rect x="20" y="39" width="5" height="5"/><rect x="29.5" y="39" width="5" height="9"/><rect x="39" y="39" width="5" height="5"/></g>
  </svg>
  <p class="step" style="left:492px;top:219px">1. Arrive before 8:30 am</p>
  <svg class="step-icon" style="left:412px;top:274px" viewBox="0 0 64 64" role="img" aria-label="Lockers icon">
    <g fill="none" stroke="#fff" stroke-width="2"><rect x="16" y="16" width="10" height="32"/><rect x="27" y="16" width="10" height="32"/><rect x="38" y="16" width="10" height="32"/></g>
  </svg>
  <p class="step" style="left:492px;top:290px">2. Drop bag at locker and<br>collect learning materials</p>
  <svg class="step-icon" style="left:412px;top:354px" viewBox="0 0 64 64" role="img" aria-label="Classroom icon">
    <rect class="thin" x="28" y="13" width="24" height="16"/>
    <circle cx="18" cy="20" r="4" fill="#fff"/>
    <path class="thin" d="M18 25V36M18 28L30 22"/>
    <g fill="#fff"><circle cx="18" cy="42" r="3.5"/><circle cx="28" cy="42" r="3.5"/><circle cx="38" cy="42" r="3.5"/><circle cx="48" cy="42" r="3.5"/>
    <path d="M13 52a5 5 0 0 1 10 0ZM23 52a5 5 0 0 1 10 0ZM33 52a5 5 0 0 1 10 0ZM43 52a5 5 0 0 1 10 0Z"/></g>
  </svg>
  <p class="step" style="left:492px;top:370px">3. Arrive at home group/<br>house assembly before 8:40 am</p>

  <div class="abs footer-text">Curiosty and Drive<small>Mervale Learner Values</small></div>
  <div class="brand" style="left:622px;top:447px"><span class="dot"></span>Mervale</div>
</section>
</body>
</html>
```